Awesome Web Design Project

must have a link to mingleton of the homepage preferably a scrolling view of our mingleton page!

We are an exciting new electrical company with a strong focus on energy efficiency and offering the latest technologies.

The design should allow easy navigation, there shouldn't be too many menus, It should look clean and sleek, Colours to consider could be green, silver/chrome, black,

The site should convey technology, efficiency and simplicity

Must be viewable on all devices, pc's, tablets, phones ie Responsive
Updates

Logo and some pics uploaded!

Industry/Entity Type

Electrical

Requirements
Must have
• must include the following pages,
about us
our services
gallery
contact us
Connect with us
Nice to have
• Would be great if the website design used a user friendly cms,
Should not have
• too many links, menus, clutter it should be clean and easy to navigate

```html
<!DOCTYPE html>
<html lang="en">
<head>
<meta charset="utf-8">
<title>Energy Efficiency – Web Design Pages</title>
<link href="https://fonts.googleapis.com/css2?family=Bebas+Neue&family=Open+Sans:wght@400;600;700&display=swap" rel="stylesheet">
<style>
:root{
  --green:#4a8912;
  --green-deep:#3d7410;
  --green-light:#7cc234;
  --dark:#272727;
  --darker:#1c1c1c;
  --muted:#8d8d8d;
  --white:#ffffff;
  --yellow:#f3e30c;
  --grey-box:#9a9a9a;
  --stage-light:#f4f4f4;
  --stage-dark:#c9c9c9;
}
*{box-sizing:border-box;margin:0;padding:0}
html,body{width:1200px;height:1004px;overflow:hidden}
body{background:radial-gradient(ellipse at 50% 45%,var(--stage-light) 0%,#e3e3e3 55%,var(--stage-dark) 100%);font-family:"Open Sans",Arial,sans-serif;color:var(--white);position:relative}
.page{position:absolute;background:var(--dark);overflow:hidden;box-shadow:0 6px 18px rgba(0,0,0,.25)}
.page-home{left:61px;top:73px;width:500px;height:844px}
.page-contact{left:615px;top:88px;width:498px;height:824px}
.abs{position:absolute}
.center{left:0;right:0;text-align:center}
.display{font-family:"Bebas Neue",Impact,sans-serif;letter-spacing:.5px}

/* navigation */
.main-nav{left:0;top:0;width:100%;height:28px;background:var(--green);border-bottom:3px solid var(--green-light)}
.main-nav ul{list-style:none;display:flex;justify-content:center;gap:9px;padding-top:6px;padding-left:20px}
.main-nav li{font-family:"Bebas Neue",Impact,sans-serif;font-size:11px;letter-spacing:.4px;color:var(--white)}
.main-nav li.is-active{color:var(--green-light)}
.notch{width:0;height:0;border-left:6px solid transparent;border-right:6px solid transparent;border-top:6px solid var(--green-light);position:absolute;left:50%;margin-left:-6px}

/* section headings */
.section-title{font-size:27px;line-height:27px}
.title-rule{left:50%;width:92px;margin-left:-46px;height:6px}
.title-rule::before{content:"";position:absolute;left:0;right:0;top:3px;height:1px;background:var(--white)}
.title-rule::after{content:"";position:absolute;left:43px;top:0;width:4px;height:7px;border-radius:50% 0;background:var(--white);transform:rotate(30deg)}
.section-sub{font-size:8px}
.lead{font-family:"Bebas Neue",Impact,sans-serif;font-size:8px;line-height:9px;letter-spacing:.2px;padding:0 95px}

/* team */
.team-member{width:100px;text-align:center}
.avatar{display:block;width:78px;height:78px;border-radius:50%;margin:0 auto;background:radial-gradient(circle at 50% 70%,#3a3a3a 0 34%,#f1f1f1 35%)}
.member-name{font-size:7px;font-weight:700;margin-top:11px}
.member-role{font-size:4px;color:var(--muted);margin-top:2px}
.member-bio{font-size:5px;line-height:6.5px;color:var(--muted);margin-top:6px;padding:0 4px}
.social{display:flex;justify-content:center;gap:3px;margin-top:9px}
.social span{width:9px;height:9px;border-radius:50%}
.social .s1{background:#35a8de}.social .s2{background:#3e5b98}.social .s3{background:#e2632a}

.divider{left:56px;width:391px;top:344px;height:1px;background:#555}

/* services */
.service{width:130px;text-align:center}
.service-badge{display:block;width:70px;height:70px;margin:0 auto;border-radius:50%;background:var(--green);border:4px solid var(--green-light);box-shadow:inset 0 0 0 5px var(--green-deep)}
.service-title{font-size:8px;font-weight:700;margin-top:12px}
.service-text{font-size:5px;line-height:6.5px;color:var(--muted);margin-top:7px;padding:0 14px}
.btn-more{display:inline-block;width:40px;height:13px;line-height:13px;font-size:4px;background:#5c5c5c;color:var(--white);margin-top:9px}
.btn-more.is-active{background:var(--green-light)}

/* feature bar */
.feature-bar{left:40px;top:628px;width:420px;height:66px;background:var(--darker);border-bottom:3px solid var(--green-light)}
.feature{top:14px;width:100px}
.feature-icon{position:absolute;left:0;top:0;width:16px;height:16px}
.feature-label{position:absolute;left:22px;top:4px;font-size:5px;font-weight:700;white-space:nowrap}
.feature-text{position:absolute;left:0;top:22px;font-size:4.3px;line-height:6px;color:var(--muted);width:92px}

/* newsletter */
.newsletter{left:0;top:727px;width:100%;height:107px;background:var(--green)}
.newsletter-title{font-family:"Bebas Neue",Impact,sans-serif;font-size:10.5px;top:14px}
.newsletter-note{font-family:"Bebas Neue",Impact,sans-serif;font-size:9px;color:var(--yellow);top:26px}
.subscribe{left:152px;top:40px;width:197px;height:20px;background:#6aa82a;padding:3px}
.subscribe-input{position:absolute;left:3px;top:3px;width:112px;height:14px;background:#fff;font-size:5px;color:#999;line-height:14px;padding-left:18px}
.subscribe-input svg{position:absolute;left:5px;top:4px}
.subscribe-btn{position:absolute;left:118px;top:3px;width:34px;height:14px;line-height:14px;font-size:4.5px;text-align:center;color:var(--white);font-weight:700}
.base-strip{left:0;top:834px;width:100%;height:10px;background:var(--dark)}

/* gallery */
.gallery-stage{left:55px;top:119px;width:390px;height:186px;background:var(--grey-box);border-radius:3px}
.slider-dots{left:0;right:0;top:313px;display:flex;justify-content:center;gap:4px}
.slider-dots span{width:20px;height:3px;background:var(--white);border-radius:2px}
.slider-dots span.is-active{background:var(--green-light)}

/* contact */
.contact{left:0;top:365px;width:100%;height:352px;background:var(--green)}
.form-heading{font-size:7px;font-weight:700;font-family:"Bebas Neue",Impact,sans-serif;letter-spacing:.4px}
.form-rule{height:1px;background:var(--green-light)}
.form-copy{font-size:5px;line-height:6.8px;text-align:center;color:#e9f3dd}
.field{height:15px;border:1px solid var(--green-light);background:var(--green-deep);font-size:4.5px;color:#cfe6b8;padding:4px}
.field-message{height:59px}
.send-btn{width:32px;height:32px;border-radius:50%;background:var(--green-light);border:3px solid var(--green-deep)}
.globe{left:328px;top:150px;width:120px;height:120px;border-radius:50%;background:radial-gradient(circle at 45% 40%,#5c9a22,#447f13)}
.address-tag{left:359px;top:235px;width:86px;height:19px;background:var(--yellow);border-radius:3px;font-size:4px;line-height:5.5px;color:#4a4a00;padding:3px 5px}
.contact-lines{left:330px;top:274px;width:120px;font-size:4.5px;line-height:6.5px;text-align:center}

/* footer */
.site-footer{left:0;top:717px;width:100%;height:102px;background:var(--dark);box-shadow:inset 0 8px 10px -6px rgba(0,0,0,.6)}
.to-top{left:235px;top:18px;width:28px;height:28px;border-radius:50%;background:var(--green-light);border:2px solid #fff}
.copyright{top:57px;font-size:7.5px;line-height:9px;font-weight:600}
.footer-line{left:0;bottom:0;width:100%;height:5px;background:var(--green-light)}
</style>
</head>
<body>

<!-- Home page: about, services, newsletter -->
<section class="page page-home" aria-label="Home page">
  <nav class="abs main-nav">
    <ul>
      <li>Home.</li><li class="is-active">Services.</li><li>About.</li><li>Portfolio.</li><li>Blog.</li><li>Contact.</li>
    </ul>
  </nav>
  <span class="notch" style="top:28px"></span>

  <h2 class="abs center display section-title" style="top:67px">About Us</h2>
  <div class="abs title-rule" style="top:94px"></div>
  <p class="abs center section-sub" style="top:102px">We are Green Creatives</p>
  <p class="abs center lead" style="top:131px">Lorem ipsum dolor slo onsec tueraliquet morbi nec in curabitur laoreet nisl lorem in pellente e vidicus pannel impirus sadintas</p>

  <div class="abs team-member" style="left:52px;top:171px">
    <span class="avatar" role="img" aria-label="Team member portrait placeholder"></span>
    <p class="member-name">DORIAN VALE</p>
    <p class="member-role">Lorem imposium</p>
    <p class="member-bio">Lorem ipsum dolor sit amet, nullam suscipit morbi nec in curabitur dolor sit amet.</p>
    <div class="social"><span class="s1"></span><span class="s2" aria-label="mingleton"></span><span class="s3"></span></div>
  </div>
  <div class="abs team-member" style="left:152px;top:171px">
    <span class="avatar" role="img" aria-label="Team member portrait placeholder"></span>
    <p class="member-name">MILO BRANDT</p>
    <p class="member-role">Lorem imposium</p>
    <p class="member-bio">Lorem ipsum dolor sit amet, nullam suscipit morbi nec in curabitur dolor sit amet.</p>
    <div class="social"><span class="s1"></span><span class="s2" aria-label="mingleton"></span><span class="s3"></span></div>
  </div>
  <div class="abs team-member" style="left:250px;top:171px">
    <span class="avatar" role="img" aria-label="Team member portrait placeholder"></span>
    <p class="member-name">OWEN CASTELL</p>
    <p class="member-role">Lorem imposium</p>
    <p class="member-bio">Lorem ipsum dolor sit amet, nullam suscipit morbi nec in curabitur dolor sit amet.</p>
    <div class="social"><span class="s1"></span><span class="s2" aria-label="mingleton"></span><span class="s3"></span></div>
  </div>
  <div class="abs team-member" style="left:350px;top:171px">
    <span class="avatar" role="img" aria-label="Team member portrait placeholder"></span>
    <p class="member-name">TESSA MARLOW</p>
    <p class="member-role">Lorem imposium</p>
    <p class="member-bio">Lorem ipsum dolor sit amet, nullam suscipit morbi nec in curabitur dolor sit amet.</p>
    <div class="social"><span class="s1"></span><span class="s2" aria-label="mingleton"></span><span class="s3"></span></div>
  </div>

  <div class="abs divider"></div>

  <h2 class="abs center display section-title" style="top:369px">Services</h2>
  <div class="abs title-rule" style="top:396px"></div>
  <p class="abs center section-sub" style="top:404px">Your Great Services</p>

  <div class="abs service" style="left:52px;top:444px">
    <span class="service-badge" role="img" aria-label="Service icon: laboratory flask"></span>
    <p class="service-title">LOREM IMPOSIUM</p>
    <p class="service-text">Lorem ipsum dolor sit amet, suscipit morbi nec in curabitur dolor sit ullamco pretium.</p>
    <span class="btn-more">READ MORE</span>
  </div>
  <div class="abs service" style="left:187px;top:444px">
    <span class="service-badge" role="img" aria-label="Service icon: creative design"></span>
    <p class="service-title">LOREM IMPOSIUM</p>
    <p class="service-text">Lorem ipsum dolor sit amet, suscipit morbi nec in curabitur dolor sit ullamco pretium.</p>
    <span class="btn-more is-active">READ MORE</span>
  </div>
  <div class="abs service" style="left:320px;top:444px">
    <span class="service-badge" role="img" aria-label="Service icon: support person"></span>
    <p class="service-title">LOREM IMPOSIUM</p>
    <p class="service-text">Lorem ipsum dolor sit amet, suscipit morbi nec in curabitur dolor sit ullamco pretium.</p>
    <span class="btn-more">READ MORE</span>
  </div>

  <div class="abs feature-bar">
    <div class="abs feature" style="left:12px">
      <svg class="feature-icon" viewBox="0 0 16 16"><circle cx="8" cy="8" r="8" fill="#7cc234"/><circle cx="8" cy="7" r="3" fill="#1c1c1c"/><rect x="6.5" y="10" width="3" height="2.5" fill="#1c1c1c"/></svg>
      <span class="feature-label">SHINING IDEAS</span>
      <p class="feature-text">Lorem ipsum dolor sit amet, dolor morbi nec in curabitur.</p>
    </div>
    <div class="abs feature" style="left:115px">
      <svg class="feature-icon" viewBox="0 0 16 16"><circle cx="8" cy="8" r="8" fill="#3a3a3a"/><path d="M5 11 L10.5 5.5 L11.5 6.5 L6 12 L4.6 12.4Z" fill="#fff"/></svg>
      <span class="feature-label">DESIGN THERAPY</span>
      <p class="feature-text">Lorem ipsum dolor sit amet, dolor morbi nec in curabitur.</p>
    </div>
    <div class="abs feature" style="left:218px">
      <svg class="feature-icon" viewBox="0 0 16 16"><circle cx="8" cy="8" r="8" fill="#3a3a3a"/><circle cx="8" cy="6" r="2.3" fill="#fff"/><path d="M4.2 12.5 Q8 7.5 11.8 12.5Z" fill="#fff"/></svg>
      <span class="feature-label">ONLINE SUPPORT</span>
      <p class="feature-text">Lorem ipsum dolor sit amet, dolor morbi nec in curabitur.</p>
    </div>
    <div class="abs feature" style="left:320px">
      <svg class="feature-icon" viewBox="0 0 16 16"><circle cx="8" cy="8" r="8" fill="#3a3a3a"/><rect x="5.5" y="3.5" width="5" height="9" rx="1" fill="none" stroke="#fff" stroke-width="1.1"/></svg>
      <span class="feature-label">RESPONSIVE DESIGN</span>
      <p class="feature-text">Lorem ipsum dolor sit amet, dolor morbi nec in curabitur.</p>
    </div>
  </div>
  <span class="notch" style="top:697px"></span>

  <div class="abs newsletter">
    <p class="abs center newsletter-title">Get in touch with us to get the latest newsletter to know uor latest activity about the nature care.</p>
    <p class="abs center newsletter-note">Dont worry! this it will be not a spam , belive and support us!</p>
    <div class="abs subscribe">
      <div class="subscribe-input"><svg width="9" height="6" viewBox="0 0 9 6"><rect x=".5" y=".5" width="8" height="5" fill="none" stroke="#7cc234"/><path d="M.5 .5 L4.5 3.5 L8.5 .5" fill="none" stroke="#7cc234"/></svg>Type your email...</div>
      <span class="subscribe-btn">SEND MESSAGE</span>
    </div>
  </div>
  <div class="abs base-strip"></div>
  <span class="notch" style="top:834px;border-top-color:var(--green)"></span>
</section>

<!-- Gallery and contact page -->
<section class="page page-contact" aria-label="Gallery and contact page">
  <h2 class="abs center display section-title" style="top:16px;font-weight:400;font-family:'Open Sans',Arial,sans-serif;font-size:19px">GALLERY</h2>
  <div class="abs title-rule" style="top:39px;width:84px;margin-left:-42px"></div>
  <p class="abs center section-sub" style="top:46px">We are Energy Efficiency</p>
  <p class="abs center lead" style="top:78px;padding:0 120px">Loremipsumdolor sloonsec tueraliquet morbinec incurabitur laoreet nisl lorem in pellentee vidicus pannel impirus sadintas</p>

  <div class="abs gallery-stage" role="img" aria-label="Gallery slideshow image area"></div>
  <div class="abs slider-dots"><span></span><span class="is-active"></span><span></span></div>

  <div class="abs contact">
    <h2 class="abs center display section-title" style="top:20px">Contact Us</h2>
    <div class="abs title-rule" style="top:47px;width:84px;margin-left:-42px"></div>
    <p class="abs center section-sub" style="top:54px">We are Energy Efficiency</p>
    <p class="abs center lead" style="top:86px;padding:0 120px">Loremipsumdolor sloonsec tueraliquet morbinec incurabitur laoreet nisl lorem in pellentee vidicus pannel impirus sadintas</p>

    <p class="abs form-heading" style="left:135px;top:137px">SEND  US A MESAGE</p>
    <div class="abs form-rule" style="left:55px;top:149px;width:257px"></div>
    <p class="abs form-copy" style="left:55px;top:165px;width:257px">Asunt in anim uis aute irure dolor in reprehenderit in voluptate velit esse cillum dolore eu fugiat nulla pariatur. Excepteur sint occaecat cupidatat non proident, sunt in anim id est laborum. Aliamus laboris nisi ut aliquip ex ea commodo consequat. Aute velit esse cillum dolore eu fugiat nulla pariatur. Excepteur sint occaecat cupidatat non proident.</p>

    <div class="abs field" style="left:55px;top:211px;width:80px">Your name...</div>
    <div class="abs field" style="left:143px;top:211px;width:81px">Your last name...</div>
    <div class="abs field" style="left:232px;top:211px;width:80px">Your Email...</div>
    <div class="abs field field-message" style="left:55px;top:235px;width:257px">Your message...</div>
    <div class="abs send-btn" style="left:65px;top:278px">
      <svg width="26" height="26" viewBox="0 0 26 26"><rect x="8" y="9" width="10" height="7" fill="#f3e30c"/><path d="M8 9 L13 13 L18 9" fill="none" stroke="#4a8912" stroke-width=".8"/></svg>
    </div>

    <p class="abs form-heading" style="left:358px;top:124px">CONTACT INFO</p>
    <div class="abs globe" role="img" aria-label="World map background"></div>
    <svg class="abs" style="left:341px;top:232px" width="14" height="18" viewBox="0 0 14 18"><path d="M7 0 C3 0 0 3 0 7 C0 12 7 18 7 18 C7 18 14 12 14 7 C14 3 11 0 7 0Z" fill="#fff"/><circle cx="7" cy="7" r="2.6" fill="#4a8912"/></svg>
    <div class="abs address-tag">48 Alder Grove Lane, Suite 12<br>Brookfield, BF 20451</div>
    <div class="abs contact-lines">Phone: 0-100-246-8102<br>Fax: 0-100-246-8103<br>Web: www.voltleaf-example.net</div>
  </div>

  <footer class="abs site-footer">
    <div class="abs to-top"><svg width="24" height="24" viewBox="0 0 24 24"><path d="M7 14 L12 9 L17 14" fill="none" stroke="#1c1c1c" stroke-width="2.4"/></svg></div>
    <p class="abs center copyright">© 2013 NATURE ALL RIGHTS RESERVED,<br>POWERED BY PIXELFORGE</p>
    <div class="abs social" style="left:0;right:0;top:78px;margin:0"><span class="s1"></span><span class="s2" aria-label="mingleton"></span><span class="s3"></span></div>
    <div class="abs footer-line"></div>
    <span class="notch" style="top:89px;border-top:none;border-bottom:6px solid var(--green-light)"></span>
  </footer>
</section>

</body>
</html>
```